Design ebook cover for my ebook and website logo. Thought Beyond Sores

This is my ebook, website, blog, and vision I have had for 24 years! Its about something that is a mystery to most of us,that is the healing power of your mind. This is both a personal account and true story. It is also a "how to" for the reader and website, blog followers. I envision words like organic, and infinite when describing this power. A theme in my book is visualzation and thoughts being pure potential energy. The book is really about consciously guiding healing throughout one's own body. A huge part of this is somethong called guided imagery. When I guided my healing, i visualized white blood cells and white light engulfing my entire body. Perhaps this can be used in the design. I also envisioned the Herpes Simplex virus as being completley destroyed by my immune system. I describe it as my mind was the commander in chief, my immune system was my battlefield general, my white blood cells were the soildiers, and the herpes simplex virus was the enemy. In my visualization, my white blood cells numbered in the trillions and the Herpes Simplex virus was very low in numbers. Our healing minds are infinitely strong. Herpes is weak by compariosn.
Good luck!

Title
Thought Beyond Sores
Sub Title
"Mending Sores Through The Force Of Thought"
Author's name Dorian P Vakely III

Target Market(s)

18 -26 year old, slightly more female to male ratio. Largest increasing population is white teenagers. New comers are in shock and looking for answers.

Font styles to use
Sans Serif

Colors
0592ce
6c459b
0455a3

Requirements
Must have
• Think organic, of nature and availbale to everyone. the power of our minds is our birthright! Its about harnessing enegy. This book at it's very core is about the power of the imagination.
Nice to have
• Please think "infinite" and "limitless." Something that immediately opens the mind of the reader at first sight. One of the themes in my book is the emotional connection with the virus
Should not have
• I dont want anything generic. Nothing man made such as machinery, plastic, exc....

```html
<!DOCTYPE html>
<html lang="en">
<head>
<meta charset="utf-8">
<title>Thought Beyond Sores – Book Cover</title>
<link rel="stylesheet" href="https://fonts.googleapis.com/css2?family=Oswald:wght@600&family=Montserrat:wght@600;700;800&display=swap">
<style>
  :root {
    --stage: #ececec;
    --ink-blue: #1b45a5;
    --band-blue: #1d48a6;
    --cover-top: #cfe2ee;
    --cover-bottom: #eef3f6;
    --back-top: #d8e7f0;
    --back-bottom: #f1f4f6;
    --spine: #e3edf3;
    --white: #ffffff;
    --photo-warm: #b9987f;
    --photo-soft: #cdb3a0;
  }
  * { margin: 0; padding: 0; box-sizing: border-box; }
  html, body { width: 1200px; height: 800px; overflow: hidden; }
  body {
    background: var(--stage);
    font-family: "Montserrat", Arial, sans-serif;
    position: relative;
  }
  .book-wrap {
    position: absolute;
    left: 178px;
    top: 100px;
    display: flex;
    height: 600px;
  }

  /* Back cover */
  .back-cover {
    width: 400px;
    height: 600px;
    position: relative;
    background: linear-gradient(180deg, var(--back-top), var(--back-bottom));
    padding: 22px 24px 0;
    color: var(--ink-blue);
  }
  .back-author {
    text-align: right;
    font-weight: 700;
    font-size: 11px;
    letter-spacing: 2px;
  }
  .back-title {
    font-family: "Oswald", "Arial Narrow", sans-serif;
    font-weight: 600;
    font-size: 33px;
    line-height: 1.1;
    text-transform: uppercase;
    text-align: center;
    white-space: nowrap;
    margin-top: 2px;
  }
  .back-subtitle {
    font-weight: 800;
    font-size: 12.5px;
    text-align: center;
    margin-top: 4px;
  }
  .back-blurb {
    margin-top: 14px;
    font-weight: 700;
    font-size: 11.5px;
    line-height: 1.4;
    text-align: justify;
    text-align-last: center;
  }
  .back-box {
    position: absolute;
    bottom: 24px;
    width: 100px;
    height: 60px;
    background: var(--band-blue);
    color: var(--white);
    font-size: 10px;
    font-weight: 600;
    display: flex;
    align-items: center;
    justify-content: center;
  }
  .back-box.logo-slot { left: 36px; }
  .back-box.isbn-slot { right: 36px; }

  /* Spine */
  .spine {
    width: 44px;
    height: 600px;
    background: var(--spine);
    color: var(--ink-blue);
    display: flex;
    flex-direction: column;
    align-items: center;
    padding: 22px 0;
    gap: 22px;
  }
  .spine-title {
    writing-mode: vertical-rl;
    font-family: "Oswald", "Arial Narrow", sans-serif;
    font-weight: 600;
    font-size: 26px;
    text-transform: uppercase;
    white-space: nowrap;
  }
  .spine-author {
    writing-mode: vertical-rl;
    font-weight: 700;
    font-size: 9px;
    letter-spacing: 3px;
    white-space: nowrap;
  }

  /* Front cover */
  .front-cover {
    width: 400px;
    height: 600px;
    position: relative;
    background: linear-gradient(180deg, var(--cover-top), var(--cover-bottom));
    overflow: hidden;
  }
  .photo-area {
    position: absolute;
    left: 82px;
    width: 236px;
    background: linear-gradient(180deg, var(--photo-warm), var(--photo-soft));
  }
  .photo-area.upper { top: 14px; height: 150px; }
  .photo-area.lower { top: 440px; height: 98px; }
  .front-title {
    position: absolute;
    left: 0; right: 0;
    top: 172px;
    text-align: center;
    font-family: "Oswald", "Arial Narrow", sans-serif;
    font-weight: 600;
    font-size: 80px;
    line-height: 1;
    text-transform: uppercase;
    color: var(--ink-blue);
  }
  .front-band {
    position: absolute;
    left: 0; right: 0; bottom: 0;
    height: 62px;
    background: var(--band-blue);
    color: var(--white);
    text-align: center;
    padding-top: 11px;
  }
  .front-subtitle {
    font-weight: 800;
    font-size: 13.5px;
  }
  .front-author {
    margin-top: 6px;
    font-weight: 700;
    font-size: 11px;
    letter-spacing: 3px;
  }
</style>
</head>
<body>
  <main class="book-wrap">
    <section class="back-cover">
      <p class="back-author">Dorian P Vakely III</p>
      <h2 class="back-title">Thought Beyond Sores</h2>
      <p class="back-subtitle">Mending Sores Through The Force Of Thought</p>
      <p class="back-blurb">This is the true story of how one young man learned to guide his own healing. Through calm breathing, steady focus and vivid guided imagery, he pictured bright white light and countless white blood cells moving through every part of his body. His mind became the commander, his immune system the general, and each cell a loyal soldier facing a small, weak enemy. Here he shares every step, from the first shock of diagnosis to the quiet strength that followed. You will learn simple daily practices, visualization scripts and ways to meet fear with patience. The power to heal is not reserved for a few. It is your birthright, open to anyone willing to imagine it. Whether you are newly diagnosed or have lived with the virus for years, these pages offer hope, clear guidance and a gentle path forward. Each chapter closes with an exercise you can practise in minutes, anywhere, with nothing but your breath and your imagination. Begin today and discover how limitless your own mind can be.</p>
      <div class="back-box logo-slot">LOGO</div>
      <div class="back-box isbn-slot">ISBN</div>
    </section>

    <section class="spine">
      <span class="spine-title">Thought Beyond Sores</span>
      <span class="spine-author">Dorian P Vakely III</span>
    </section>

    <section class="front-cover">
      <div class="photo-area upper" role="img" aria-label="Photo placeholder: upper part of a young man's head lifted away like a lid"></div>
      <div class="photo-area lower" role="img" aria-label="Photo placeholder: lower part of the same head, looking upward"></div>
      <h1 class="front-title">Thought<br>Beyond<br>Sores</h1>
      <div class="front-band">
        <p class="front-subtitle">Mending Sores Through The Force Of Thought</p>
        <p class="front-author">Dorian P Vakely III</p>
      </div>
    </section>
  </main>
</body>
</html>
```